Design a New Tennis and Athletic Club- Business cards desired with a wow factor.

Help us find a exciting and useful design for our business.
1. Design should be two-sided made of materials that will last.
2. Eye-popping graphics
3. Space for changeable quotes on the back of our card with our "wolf" program logo.
4. Recolor wolf to match club colors

Target Market(s)

Players parents coaches clients

Industry/Entity Type

Business

Contact Information for Business Card

Birchwood Paddle + Wellness
Derek Hollins
Director of Tennis Operations
2817 Meadowcrest Ave NE
Grand Rapids Michigan 49318
Office (616) 555-0142
Cell (269) 555-0186
Email dhollins482@mailbox-example.com
Website http://www.bwpaddle-example.com
Facebook https://www.facebook.com/BWPaddleExample

Font styles to use
Serif

Colors
0555a3
f37122
ffffff

Requirements
Must have
• 1.interesting contemporary design,
• 2. 2 sided
• 3. ability to swap out staff information for other trainers and professionals
Nice to have
• 1.Space for changeable quotes on the back of the card
• 2. change wolf logo body to match club color blue
• 3. some white space on card for notes to be written.
Should not have
• boring same old consruction

```html
<!DOCTYPE html>
<html lang="en">
<head>
<meta charset="utf-8">
<title>Birchwood Paddle + Wellness — Business Card</title>
<link rel="stylesheet" href="https://fonts.googleapis.com/css2?family=Questrial&display=swap">
<style>
  :root {
    --stage: #1a1a1a;
    --navy: #272b5e;
    --orange: #f37122;
    --orange-light: #f7a43c;
    --white: #ffffff;
    --wolf-blue: #0555a3;
    --ink-soft: #d9dbe8;
    --ink-grey: #555a6a;
  }
  * { box-sizing: border-box; margin: 0; padding: 0; }
  html, body {
    width: 1200px; height: 864px; overflow: hidden;
    background: var(--stage);
    font-family: "Questrial", "Century Gothic", sans-serif;
  }
  .stage {
    position: relative; width: 1200px; height: 864px;
    display: flex; align-items: center; justify-content: center; gap: 40px;
  }
  .card {
    position: relative; width: 540px; height: 308px; overflow: hidden;
    background: var(--white); border-radius: 3px;
  }
  .card-shapes { position: absolute; inset: 0; width: 100%; height: 100%; }

  /* Front */
  .brand {
    position: absolute; top: 58px; left: 0; right: 0; text-align: center;
    color: var(--navy); font-size: 22px; letter-spacing: 0.5px;
  }
  .brand-mark {
    display: block; width: 14px; height: 14px; margin: 0 auto 10px;
    border-radius: 50%; background: var(--navy);
  }
  .staff { position: absolute; left: 24px; top: 198px; color: var(--white); }
  .staff-name { font-size: 15px; letter-spacing: 1.5px; text-transform: uppercase; }
  .staff-title { font-size: 13px; color: var(--orange-light); margin-top: 2px; }
  .staff-address { font-size: 13px; line-height: 1.35; margin-top: 8px; color: var(--ink-soft); }
  .contact {
    position: absolute; right: 22px; top: 226px; list-style: none;
    color: var(--white); font-size: 13px; text-align: right;
  }
  .contact li { display: flex; align-items: center; justify-content: flex-end; gap: 8px; line-height: 20px; }
  .contact-icon {
    width: 15px; height: 15px; border-radius: 50%; background: #c9cbd8;
    display: inline-flex; align-items: center; justify-content: center;
  }
  .contact-icon svg { width: 9px; height: 9px; }

  /* Back */
  .mascot {
    position: absolute; left: 250px; top: 24px; width: 150px; height: 108px;
    border-radius: 40% 55% 35% 45%;
    background: radial-gradient(circle at 45% 50%, var(--orange) 0 30%, var(--wolf-blue) 60%, #1a3f8a 100%);
  }
  .program-name {
    position: absolute; left: 0; right: 0; top: 206px; text-align: center;
    font-size: 28px; color: var(--orange); letter-spacing: 2px;
    text-transform: uppercase; line-height: 1;
  }
  .website {
    position: absolute; left: 0; right: 0; bottom: 28px; text-align: center;
    color: var(--ink-grey); font-size: 15px; letter-spacing: 0.5px;
  }
</style>
</head>
<body>
<main class="stage">

  <section class="card card-front" aria-label="Business card front">
    <svg class="card-shapes" viewBox="0 0 540 308" preserveAspectRatio="none" aria-hidden="true">
      <path d="M0,184 Q270,132 540,206 L540,308 L0,308 Z" fill="var(--navy)"/>
      <path d="M0,172 Q270,112 540,194 L540,200 Q270,130 0,178 Z" fill="var(--orange-light)"/>
    </svg>
    <div class="brand"><span class="brand-mark"></span>Birchwood Paddle + Wellness</div>
    <div class="staff">
      <p class="staff-name">Derek Hollins</p>
      <p class="staff-title">Director of Tennis Operations</p>
      <p class="staff-address">2817 Meadowcrest Ave NE<br>Grand Rapids Michigan 49318</p>
    </div>
    <ul class="contact">
      <li>(616) 555-0142
        <span class="contact-icon"><svg viewBox="0 0 10 10"><path d="M1,3 Q1,1 3,1 L7,1 Q9,1 9,3 L9,4 L7,4 L7,3 L3,3 L3,4 L1,4 Z M2,5 L8,5 L9,9 L1,9 Z" fill="var(--navy)"/></svg></span></li>
      <li>(269) 555-0186
        <span class="contact-icon"><svg viewBox="0 0 10 10"><path d="M2,1 L4,1 L4.5,3.5 L3.5,4.2 Q4.5,6 5.8,6.5 L6.5,5.5 L9,6 L9,8 Q8,9 6.5,9 Q1,7.5 1,2.5 Q1,1 2,1 Z" fill="var(--navy)"/></svg></span></li>
      <li>dhollins482@mailbox-example.com
        <span class="contact-icon"><svg viewBox="0 0 10 10"><rect x="1" y="2.5" width="8" height="5.5" fill="none" stroke="var(--navy)" stroke-width="1"/><path d="M1,2.5 L5,5.5 L9,2.5" fill="none" stroke="var(--navy)" stroke-width="1"/></svg></span></li>
    </ul>
  </section>

  <section class="card card-back" aria-label="Business card back">
    <svg class="card-shapes" viewBox="0 0 540 308" preserveAspectRatio="none" aria-hidden="true">
      <path d="M0,0 L540,0 L540,250 Q330,120 0,118 Z" fill="var(--navy)"/>
      <path d="M0,118 Q330,120 540,250 L540,258 Q330,132 0,126 Z" fill="var(--orange)"/>
    </svg>
    <div class="mascot" role="img" aria-label="Program mascot illustration: a blue and orange wolf running with a tennis ball"></div>
    <p class="program-name">Northstar Tennis</p>
    <p class="website">www.bwpaddle-example.com</p>
  </section>

</main>
</body>
</html>
```